We are looking to have a very professional, simple, and timeless design for a brochure that we will be handing out personally to possible clients. We are looking for something NEW , FRESH, and INNOVATIVE, but NOT TRENDY. We have already purchased a business card design from pixel meadow. The only thing that must stay the same is the type of font "K.L. Bookkeeping Services" is in. The files below are ideas we have used or liked and are wanting something of that nature for the brochure. If you have any questions please feel free to email me.

```html
<!DOCTYPE html>
<html lang="en">
<head>
<meta charset="utf-8">
<title>K.L. Bookkeeping Services – Brochure</title>
<link rel="stylesheet" href="https://fonts.googleapis.com/css2?family=Didact+Gothic&family=Mulish:wght@700&display=swap">
<style>
  :root {
    --page-bg: #d9d9d9;
    --ink: #1b1b1b;
    --black: #0b0b0b;
    --panel-light: #f4f4f4;
    --panel-mid: #c9c9c9;
    --muted: #bdbdbd;
    --white: #ffffff;
  }
  * { box-sizing: border-box; margin: 0; padding: 0; }
  html, body { width: 872px; height: 1200px; overflow: hidden; background: var(--page-bg); }
  .brochure {
    position: absolute; left: 0; top: 20px; width: 872px; height: 1160px;
    background: var(--black); overflow: hidden;
    font-family: "Didact Gothic", "Century Gothic", sans-serif; color: var(--ink);
  }
  .hero {
    position: absolute; left: 0; top: 0; width: 872px; height: 342px;
    background: linear-gradient(180deg, #f1efec 0%, #bdb8b2 45%, #77726c 80%, #4d4a46 100%);
  }
  .hero-fade {
    position: absolute; left: 0; top: 0; width: 288px; height: 342px;
    background: linear-gradient(180deg, rgba(255,255,255,.85), rgba(255,255,255,.25));
  }
  .brand {
    position: absolute; left: 28px; top: 36px; width: 260px;
    font-size: 40px; line-height: 1.05; color: var(--ink);
  }
  .panel {
    position: absolute; left: 40px;
    background: linear-gradient(90deg, var(--panel-light) 0%, #e2e2e2 60%, var(--panel-mid) 100%);
  }
  .about { top: 349px; width: 793px; height: 125px; padding: 10px 22px; font-size: 16.5px; line-height: 19.5px; }
  .services { top: 492px; width: 793px; height: 300px; padding: 10px 26px; }
  .software { top: 804px; width: 832px; height: 199px; padding: 6px 26px; }
  .panel-title { font-family: "Mulish", sans-serif; font-weight: 700; font-size: 24px; line-height: 28px; }
  .columns { display: flex; }
  .columns ul { list-style: none; }
  .services .columns ul { font-size: 16.5px; line-height: 19.8px; }
  .services .columns ul:first-child { width: 342px; }
  .software .columns ul { font-size: 16.5px; line-height: 17.9px; }
  .software .columns ul:first-child { width: 342px; }
  .columns li::before { content: "\2022\00a0"; }
  .laptop { position: absolute; right: 18px; top: 10px; }
  .contact {
    position: absolute; left: 21px; top: 1018px; width: 286px; height: 116px;
    background: linear-gradient(90deg, #f2f2f2, #cfcfcf); padding: 6px 18px;
  }
  .contact-line { display: flex; align-items: center; gap: 6px; font-size: 19px; line-height: 27px; }
  .aside { position: absolute; left: 343px; top: 1022px; width: 520px; color: var(--white); }
  .aside .panel-title { color: var(--white); }
  .aside p { font-size: 14.5px; color: var(--muted); line-height: 19px; margin-bottom: 14px; }
</style>
</head>
<body>
<main class="brochure">
  <div class="hero" role="img" aria-label="Black and white photograph of a downtown Nashville street with historic storefronts and a tall tower"></div>
  <div class="hero-fade"></div>
  <div class="brand">K.L. Bookkeeping Services</div>

  <section class="panel about">
    K.L. Bookkeeping Services is a full service bookkeeping solutions company in Nashville, Tennessee. We provide experienced, affordable and dependable bookkeeping services to businesses in the Middle Tennessee area. We have over 30 years’ experience in the bookkeeping field. This allows us to take care of your books, so you can concentrate on your business, while generating profits.
  </section>

  <section class="panel services">
    <h2 class="panel-title">Services</h2>
    <div class="columns">
      <ul>
        <li>Account Analysis</li><li>Accounts Payable</li><li>Accounts Receivable</li>
        <li>Annual &amp; Monthly Budgets</li><li>Audit Preparation</li><li>Balance Sheet</li>
        <li>Bank Deposits</li><li>Bank Reconciliations</li><li>Consulting</li>
        <li>Corporate Tax Return Preparation</li><li>Credit Card Reconciliations</li><li>Evaluate Accounting Software</li>
      </ul>
      <ul>
        <li>Inventory</li><li>Invoicing</li><li>Loan Schedules</li><li>Payroll</li>
        <li>Payroll Tax Returns</li><li>Personal Tax Return</li><li>Prepare W’2s and 1099’s</li>
        <li>Present Financials to Boards, Committees, etc.</li><li>Profit &amp; Loss Statements</li>
        <li>Property Tax Returns</li><li>Small Business Loan Paperwork</li><li>Variance Analysis</li>
      </ul>
    </div>
  </section>

  <section class="panel software">
    <svg class="laptop" width="200" height="190" viewBox="0 0 200 190" aria-hidden="true">
      <rect x="28" y="10" width="144" height="110" rx="6" fill="none" stroke="#b3b3b3" stroke-width="8"/>
      <path d="M8 140 H192 L180 160 H20 Z" fill="#b3b3b3"/>
    </svg>
    <h2 class="panel-title">Software</h2>
    <div class="columns">
      <ul>
        <li>LedgerLeaf</li><li>LedgerLeaf Online</li><li>Paydeck - Payroll</li>
        <li>Paydeck - Auto Dealership Software</li><li>Veridane</li><li>Broad Fields</li>
        <li>Hearth Accounting Solutions</li><li>Tallyra</li><li>QRX</li>
      </ul>
      <ul>
        <li>NAV 70</li><li>Dorrin Data Systems</li><li>Paymint</li><li>Payrove</li>
        <li>Plumgrove</li><li>Thymeline</li><li>Corvio</li><li>RAL</li><li>Swiftly</li>
      </ul>
    </div>
  </section>

  <section class="contact">
    <h2 class="panel-title">Contact Us</h2>
    <div class="contact-line">
      <svg width="16" height="14" viewBox="0 0 16 14" aria-hidden="true"><path d="M1 4 Q8 -1 15 4 L13 6 L11 4 H5 L3 6 Z M4 7 H12 L14 13 H2 Z" fill="#1b1b1b"/></svg>
      615 555 0148
    </div>
    <div class="contact-line">
      <svg width="18" height="13" viewBox="0 0 18 13" aria-hidden="true"><rect x="0.5" y="0.5" width="17" height="12" fill="#1b1b1b"/><path d="M1 1 L9 7 L17 1" fill="none" stroke="#eee" stroke-width="1.2"/></svg>
      kl@klbkservices.com
    </div>
    <div class="contact-line">
      <svg width="16" height="16" viewBox="0 0 16 16" aria-hidden="true"><circle cx="8" cy="8" r="7.5" fill="#1b1b1b"/><path d="M1 8 H15 M8 1 Q3 8 8 15 M8 1 Q13 8 8 15" fill="none" stroke="#eee" stroke-width="1"/></svg>
      www.klbkservices.com
    </div>
  </section>

  <section class="aside">
    <h2 class="panel-title">Pricing</h2>
    <p>* Flexible hourly, monthly, and project rates are available</p>
    <h2 class="panel-title">References</h2>
    <p>References available upon request. Give us a call to learn more.</p>
  </section>
</main>
</body>
</html>
```